New Property management company business cards

Looking for a new business card, to reflect new younger ownership
Card should be clean, simple and professional but with a modern layout that is conveys our new logo and business model

Key aspects of the business:

Property Management
Facility Maintenance
Project Management
Tenant Improvements

Mailing Address:
PO BOX 7186
Modesto CA, 95353

Phone: 209-614-8837
Direct: 209-614-8831

Doyle Farrant
President

Target Market(s)

Commercial property owners

Industry/Entity Type

Real Estate property management

Contact Information for Business Card

Open to all designs but lean toward vertical layouts

Requirements
Must have
• Logo and space to customize name and contact info

```html
<!DOCTYPE html>
<html lang="en">
<head>
<meta charset="utf-8">
<title>Veranta Property Management – Business Card</title>
<link rel="stylesheet" href="https://fonts.googleapis.com/css2?family=Poppins:wght@300;400;500&family=Gilda+Display&display=swap">
<style>
  :root {
    --ink: #33333f;
    --teal: #1fb0a6;
    --navy: #263562;
    --paper: #ffffff;
    --gap: #000000;
  }
  * { margin: 0; padding: 0; box-sizing: border-box; }
  html, body { width: 1200px; height: 981px; overflow: hidden; background: var(--gap); }
  .stage {
    position: absolute; left: 0; top: 0;
    width: 1284px; height: 1050px;
    transform: scale(0.93458); transform-origin: 0 0;
    font-family: "Poppins", sans-serif;
  }
  .card { position: absolute; top: 0; height: 1050px; overflow: hidden; }
  .card-front { left: 0; width: 600px; background: var(--paper); }
  .card-back { left: 683px; width: 601px; background: var(--navy); }
  .card-back .header { position: absolute; left: 0; top: 0; width: 100%; height: 400px; background: var(--paper); }

  .brand { position: absolute; left: 0; width: 100%; text-align: center; color: var(--ink); font-weight: 500; }
  .brand-square { display: block; margin: 0 auto; background: var(--teal); }
  .brand-name { display: block; line-height: 1; }
  .brand-tagline { display: block; line-height: 1; }

  .card-front .brand { top: 170px; }
  .card-front .brand-square { width: 56px; height: 56px; margin-bottom: 44px; }
  .card-front .brand-name { font-size: 66px; letter-spacing: 0.14em; padding-left: 0.14em; }
  .card-front .brand-tagline { font-size: 20px; letter-spacing: 0.42em; padding-left: 0.42em; margin-top: 16px; }

  .card-back .brand { top: 130px; }
  .card-back .brand-square { width: 46px; height: 46px; margin-bottom: 44px; }
  .card-back .brand-name { font-size: 54px; letter-spacing: 0.14em; padding-left: 0.14em; }
  .card-back .brand-tagline { font-size: 16px; letter-spacing: 0.42em; padding-left: 0.42em; margin-top: 12px; }

  .stripes { position: absolute; left: 0; top: 0; }

  .person { position: absolute; top: 550px; left: 0; width: 100%; text-align: center; color: var(--teal); }
  .person-name { font-family: "Gilda Display", serif; font-size: 46px; font-weight: 400; line-height: 1; text-transform: uppercase; }
  .person-title { font-size: 24px; font-weight: 400; letter-spacing: 0.1em; margin-top: 4px; }

  .services { position: absolute; top: 718px; left: 0; width: 100%; text-align: center; color: var(--teal); }
  .services-heading { font-family: "Gilda Display", serif; font-size: 22px; font-weight: 400; text-transform: uppercase; }
  .services-list { font-size: 14px; font-weight: 300; letter-spacing: 0.1em; line-height: 18px; margin-top: 4px; }

  .contact-icon { position: absolute; left: 82px; width: 45px; height: 45px; border-radius: 50%; background: var(--teal); }
  .contact-icon svg { display: block; }
  .icon-phone { top: 856px; }
  .icon-pin { top: 948px; }
  .phones { position: absolute; top: 874px; right: 80px; text-align: right; color: var(--teal); font-size: 21px; letter-spacing: 0.13em; line-height: 29px; }
  .address { position: absolute; top: 956px; left: 162px; color: var(--teal); font-size: 20px; line-height: 1; }
</style>
</head>
<body>
<main class="stage">
  <section class="card card-front">
    <div class="brand">
      <span class="brand-square"></span>
      <span class="brand-name">VERANTA</span>
      <span class="brand-tagline">PROPERTY MANAGEMENT</span>
    </div>
    <svg class="stripes" width="600" height="1050" viewBox="0 0 600 1050" aria-hidden="true">
      <polygon points="0,393 0,510 316,828 436,828" fill="var(--ink)"/>
      <polygon points="0,610 0,728 60,787 178,787" fill="var(--teal)"/>
      <polygon points="60,868 178,868 0,1046 0,928" fill="var(--teal)"/>
    </svg>
  </section>

  <section class="card card-back">
    <div class="header">
      <div class="brand">
        <span class="brand-square"></span>
        <span class="brand-name">VERANTA</span>
        <span class="brand-tagline">PROPERTY MANAGEMENT</span>
      </div>
    </div>

    <div class="person">
      <h1 class="person-name">Doyle Farrant</h1>
      <p class="person-title">President</p>
    </div>

    <div class="services">
      <h2 class="services-heading">Key aspects of the business:</h2>
      <p class="services-list">Property Management | Facility Maintenance<br>Project Management | Tenant Improvements</p>
    </div>

    <span class="contact-icon icon-phone">
      <svg width="45" height="45" viewBox="0 0 45 45" aria-hidden="true">
        <path d="M15 12c1.5-1 3-.5 3.6.8l1.6 3.6c.4 1-.1 2-1 2.6l-1.4.9c1 2.6 3 4.7 5.6 5.8l1-1.3c.6-.9 1.7-1.2 2.6-.8l3.5 1.7c1.2.6 1.6 2.2.6 3.6-1.3 1.8-3.4 2.6-5.6 1.8C18.7 28.4 15.4 24.8 13.5 18.9c-.7-2.4.1-5.3 1.5-6.9z" fill="var(--navy)"/>
        <path d="M25 12a8 8 0 0 1 8 8M25 16a4 4 0 0 1 4 4" stroke="var(--navy)" stroke-width="1.6" fill="none" stroke-linecap="round"/>
      </svg>
    </span>
    <p class="phones">209-614-8837<br>209-614-8831</p>

    <span class="contact-icon icon-pin">
      <svg width="45" height="45" viewBox="0 0 45 45" aria-hidden="true">
        <path d="M22.5 10c-5 0-8.5 3.7-8.5 8.3 0 5.8 8.5 15.7 8.5 15.7s8.5-9.9 8.5-15.7C31 13.7 27.5 10 22.5 10z" fill="var(--navy)"/>
        <circle cx="22.5" cy="18.5" r="3.2" fill="var(--teal)"/>
      </svg>
    </span>
    <p class="address">PO BOX 7186, Modesto CA, 95353</p>
  </section>
</main>
</body>
</html>
```